New Website for ReBranded Company - CrewBeacon

We have a successful company and website currently but it is a little dated. We have re-branded the company from Harbor Signal Networks to CrewBeacon and have a new logo for the new name. We are looking to build a newer fresher website with the new name. I will need a concept of the home page and one inside page. You can see our current site at https://www.harborsignalnetworks.example and the new site will be https://www.crewbeacon.example .

I also really like the https://www.pathlantern.example/ website. I like ledgerkite.example website. I like the https://skillorbit.example/ website.

See the attached document for layout and some text to use. Use the pictures I attached as opposed to pictures from the old site as much as you can.

Target Market(s)

Business

Industry/Entity Type

Software Service

Number of Pages Required

2 page

Font styles to use
Sans Serif

Requirements
Must have
• Use the colors from my logo. Professional but modern. We want people to feel like our product makes their staff feel safer at work.
Should not have
• Don't use any red or orange (no stop colors).

```html
<!DOCTYPE html>
<html lang="en">
<head>
<meta charset="utf-8">
<title>CrewBeacon – Get Help Fast</title>
<link href="https://fonts.googleapis.com/css2?family=Catamaran:wght@400;500;600;700&family=Lato:wght@400;700&display=swap" rel="stylesheet">
<style>
:root{
  --blue:#2b7fc8;
  --blue-deep:#1f6fb6;
  --green:#6cb33f;
  --ink:#1e1e1e;
  --text:#444;
  --muted:#f2f2f2;
  --hero-a:#3a3a38;
  --hero-b:#5a5c55;
}
*{box-sizing:border-box;margin:0;padding:0}
html,body{width:1200px;height:3682px;overflow:hidden}
body{font-family:"Lato",sans-serif;color:var(--text);background:#fff;position:relative}
.head,.alt{font-family:"Catamaran",sans-serif}
.wrap{width:1022px;margin:0 auto;position:relative}
.btn{display:inline-block;font-family:"Catamaran",sans-serif;text-transform:uppercase;color:#fff;background:var(--green);text-decoration:none;text-align:center}
.btn.ghost{background:transparent;border:3px solid #fff}
.chev{color:var(--green);margin-right:10px}

/* header */
.site-header{height:119px;display:flex;align-items:center}
.site-header .wrap{display:flex;align-items:center;height:119px}
.brand{display:flex;align-items:center;gap:14px;text-decoration:none}
.brand-dot{width:70px;height:70px;border-radius:50%;background:var(--blue)}
.brand-name{font-family:"Catamaran",sans-serif;font-weight:600;font-size:40px;color:var(--blue)}
.nav{display:flex;gap:28px;margin-left:118px}
.nav a{font-family:"Catamaran",sans-serif;font-weight:700;font-size:15px;color:var(--ink);text-decoration:none;padding-bottom:6px}
.nav a.active{border-bottom:3px solid var(--blue)}
.site-header .btn{margin-left:auto;font-size:15px;font-weight:700;width:215px;height:52px;line-height:52px}

/* hero */
.hero{height:582px;background:linear-gradient(120deg,var(--hero-a),var(--hero-b) 55%,#46483f);text-align:center;color:#fff;padding-top:160px}
.hero h1{font-family:"Catamaran",sans-serif;font-weight:500;font-size:48px;line-height:54px}
.hero p{font-size:23px;margin-top:18px}
.hero .btn{font-size:22px;width:186px;height:62px;line-height:62px;margin-top:36px}

/* features */
.features{display:flex;gap:16px;margin-top:93px}
.feature{width:330px;height:123px;display:flex;align-items:center;padding:0 14px;gap:18px;font-family:"Catamaran",sans-serif;font-size:16px;line-height:27px}
.feature.grey{background:var(--muted);color:var(--ink)}
.feature.green{background:var(--green);color:#fff}
.feature.blue{background:var(--blue);color:#fff}
.feature svg{flex:none}

/* help band */
.help-band{margin-top:90px;height:316px;background:linear-gradient(90deg,#2a7ec9,#3187cf);color:#fff;text-align:center;padding-top:62px}
.help-band h2{font-family:"Catamaran",sans-serif;font-weight:500;font-size:32px}
.help-band .lead{font-size:22px;margin-top:4px}
.help-band .sub{font-size:19px;margin-top:12px}
.help-band .btn{font-size:20px;width:200px;height:54px;line-height:48px;margin-top:24px}

/* why */
.section-title{font-family:"Catamaran",sans-serif;font-weight:500;font-size:37px;color:var(--ink);text-align:center;text-transform:uppercase}
.why{padding-top:84px;text-align:center}
.cards{display:flex;gap:29px;margin-top:30px;text-align:left}
.card{width:321px;height:384px;background:var(--muted);box-shadow:2px 2px 3px rgba(0,0,0,.25);padding:10px 11px}
.card .photo{height:177px}
.card h3{font-family:"Lato",sans-serif;font-weight:400;font-size:16px;color:var(--green);margin:18px 0 16px}
.card p{font-size:14px;line-height:27px;color:#444}
.card.cost{padding-left:21px}
.opts{display:grid;grid-template-columns:125px 110px 60px;font-size:14px;line-height:32px;margin-top:2px}
.why .btn{font-size:17px;width:181px;height:50px;line-height:50px;margin-top:49px;position:relative;left:13px}

/* stats */
.stats{margin-top:92px;height:258px;background:linear-gradient(90deg,#2b80c9,#2f86cd);color:#fff;display:flex}
.stats .half{width:600px;text-align:center;font-family:"Catamaran",sans-serif}
.stats .left{padding-top:66px;border-right:1px solid rgba(255,255,255,.6)}
.stats .left p{font-size:23px;line-height:32px}
.stats .left .btn{font-size:18px;width:181px;height:55px;line-height:49px;margin-top:32px}
.stats .right{padding-top:60px}
.stats .right p{font-size:23px;line-height:32px}
.nums{display:flex;justify-content:center;gap:0;margin-top:8px}
.num{width:143px}
.num b{display:block;font-weight:500;font-size:48px;line-height:52px}
.num span{font-size:24px}

/* plan */
.plan{padding-top:96px;text-align:center}
.plan-cols{display:flex;gap:37px;margin-top:36px;text-align:left}
.plan-col{width:316px}
.plan-col .photo{height:214px}
.plan-col h3{font-family:"Catamaran",sans-serif;font-weight:500;font-size:22px;color:var(--green);margin-top:18px;line-height:31px}
.plan-col ul{list-style:none;margin-top:36px;font-size:17px;line-height:32px;color:#555}
.plan-col p{font-size:16px;line-height:31px;color:#555;margin-top:8px}
.plan .btn{font-size:18px;width:196px;height:53px;line-height:53px;margin-top:36px}

/* cta strip */
.cta-strip{margin-top:90px;height:94px;background:#efefef}
.cta-strip .wrap{display:flex;align-items:center;height:94px}
.cta-strip p{font-family:"Catamaran",sans-serif;font-weight:500;font-size:20px;color:var(--ink)}
.cta-strip .btn{margin-left:auto;font-size:17px;width:164px;height:50px;line-height:50px}

/* footer */
.site-footer{height:438px}
.site-footer .wrap{display:flex;padding-top:78px}
.foot-about{width:434px}
.foot-about h2{font-family:"Catamaran",sans-serif;font-weight:700;font-size:28px;color:var(--ink)}
.foot-about p{font-size:16px;line-height:32px;color:#555;margin-top:30px;width:350px;text-align:justify}
.foot-about .brand{margin-top:24px}
.foot-about .brand-dot{width:62px;height:62px}
.foot-about .brand-name{font-size:36px}
.foot-col{width:203px}
.foot-col h3{font-family:"Catamaran",sans-serif;font-weight:500;font-size:20px;color:var(--ink);margin-top:4px}
.foot-col ul{list-style:none;margin-top:26px;font-size:16px;line-height:32px;color:var(--ink)}
.site-bottom{position:absolute;left:0;top:3621px;width:1200px;height:61px;background:var(--blue);color:#fff;text-align:center;line-height:61px;font-family:"Catamaran",sans-serif;font-size:19px}
</style>
</head>
<body>

<header class="site-header">
  <div class="wrap">
    <a class="brand" href="#"><span class="brand-dot"></span><span class="brand-name">CrewBeacon</span></a>
    <nav class="nav">
      <a class="active" href="#">HOME</a>
      <a href="#">BUY ADDONS</a>
      <a href="#">CUST LOGIN</a>
    </nav>
    <a class="btn" href="#">Explore your choices</a>
  </div>
</header>

<section class="hero" role="img" aria-label="Photo of a hand pressing a panic button mounted under a desk">
  <h1>FEEL CONFIDENT THAT YOUR<br>STAFF IS PROTECTED</h1>
  <p>Get a revolutionary new electronic panic button</p>
  <a class="btn" href="#">Get started</a>
</section>

<div class="wrap features">
  <div class="feature grey">
    <svg width="66" height="66" viewBox="0 0 66 66" fill="none" stroke="#222" stroke-width="2.5"><rect x="8" y="14" width="22" height="46"/><rect x="36" y="6" width="22" height="54"/><path d="M13 22h5M22 22h4M13 32h5M22 32h4M41 14h5M50 14h4M41 24h5M50 24h4M41 34h5M50 34h4M4 60h58"/></svg>
    <span>Problems Stopped Before They Start For Any Type Of Organization</span>
  </div>
  <div class="feature green">
    <svg width="62" height="62" viewBox="0 0 62 62" fill="none" stroke="#fff" stroke-width="3"><circle cx="31" cy="31" r="28"/><path d="M38 22c-2-3-12-4-13 2s13 5 13 11-11 6-14 2M31 14v34"/></svg>
    <span>Affordable Prices Starting at $18 per month. No Contracts . No Hidden Costs.</span>
  </div>
  <div class="feature blue">
    <svg width="62" height="62" viewBox="0 0 62 62" fill="none" stroke="#fff" stroke-width="3" stroke-linejoin="round"><path d="M31 6L58 54H4z"/><path d="M31 24v16M31 45v3"/></svg>
    <span>Alerts by computer, mobile device, text, phone, email, monitoring and E911</span>
  </div>
</div>

<section class="help-band" role="img" aria-label="Blue-tinted photo of a desk phone with a panic button">
  <h2>Your Employees Shouldn’t Feel Alone When They Need Help</h2>
  <p class="lead">Does this problem make you feel frustrated and anxious?</p>
  <p class="sub">Put a simple solution in their hands</p>
  <a class="btn ghost" href="#">Get started</a>
</section>

<section class="why">
  <h2 class="section-title">Why busineses choose us</h2>
  <div class="wrap cards">
    <article class="card">
      <div class="photo" role="img" aria-label="Hand reaching for a button under a desk" style="background:linear-gradient(135deg,#2c2c2c,#6e6e66 60%,#b9b9b0)"></div>
      <h3>EASY TO USE</h3>
      <p style="text-align:justify">Press A Button And Let The Right People Know You Need Help And Open A Chat Window Letting Everyone Talk On Resolving Their Problem.</p>
    </article>
    <article class="card">
      <div class="photo" role="img" aria-label="Office desk phone beside a panic button" style="background:linear-gradient(135deg,#8a9a8c,#3a3d3f 55%,#202226)"></div>
      <h3>COMMUNICATE THE WAY YOU WANT</h3>
      <p style="font-size:13px">We give you lots of options:</p>
      <div class="opts">
        <span><span class="chev">›</span>Computer</span><span><span class="chev">›</span>Call Center</span><span><span class="chev">›</span>Email</span>
        <span><span class="chev">›</span>Mobile</span><span><span class="chev">›</span>Text</span><span></span>
        <span><span class="chev">›</span>Phone call</span><span><span class="chev">›</span>E911</span><span></span>
      </div>
    </article>
    <article class="card cost">
      <div class="photo" role="img" aria-label="Hand holding a small alert fob by a jeans pocket" style="background:linear-gradient(135deg,#1d2c4a,#34507e 55%,#1a2640)"></div>
      <h3>COST EFFECTIVE PROTECTION</h3>
      <p style="text-align:justify">By leveraging your existing network and equipment we can lower your costs to give better options to your staff.</p>
    </article>
  </div>
  <a class="btn" href="#">Get started</a>
</section>

<section class="stats">
  <div class="half left">
    <p>We know how scary it can feel to worry<br>about employee safety.</p>
    <a class="btn ghost" href="#">Start my demo</a>
  </div>
  <div class="half right">
    <p>That’s why we have provided a way for<br>customers to get help to staff effectively in</p>
    <div class="nums">
      <div class="num"><b>45</b><span>States</span></div>
      <div class="num"><b>15</b><span>Covering</span></div>
      <div class="num"><b>5</b><span>Countries</span></div>
    </div>
  </div>
</section>

<section class="plan">
  <h2 class="section-title">Simple start plan</h2>
  <div class="wrap plan-cols">
    <div class="plan-col">
      <div class="photo" role="img" aria-label="Panic button mounted on a wall" style="background:linear-gradient(90deg,#3a3a3a,#9a9a96 50%,#5a5a58)"></div>
      <h3>Explore Your Choices</h3>
      <ul><li><span class="chev">›</span>Pricing</li><li><span class="chev">›</span>Trial</li><li><span class="chev">›</span>Quote</li><li><span class="chev">›</span>Hardware</li></ul>
    </div>
    <div class="plan-col">
      <div class="photo" role="img" aria-label="Hand holding a panic button device" style="background:linear-gradient(90deg,#5d6a72,#2a2a2a 50%,#7a8a90)"></div>
      <h3>Get Setup</h3>
      <ul><li><span class="chev">›</span>Input Your Alerts</li><li><span class="chev">›</span>Input Your Staff</li><li><span class="chev">›</span>Install Our Software</li></ul>
    </div>
    <div class="plan-col">
      <div class="photo" role="img" aria-label="Alert fob on a lanyard beside a sticky note" style="background:linear-gradient(90deg,#6a6e6a,#8a8c88 60%,#5c5e5a)"></div>
      <h3>Feel Confident Your Staff Is Protected</h3>
      <p>High Five. You just too a major step to getting rid of the anxiety and frustration this gave you.</p>
    </div>
  </div>
  <a class="btn" href="#">Start my demo</a>
</section>

<section class="cta-strip">
  <div class="wrap">
    <p>Stay Connected with Staff during a Crisis Situations</p>
    <a class="btn" href="#">Start my demo</a>
  </div>
</section>

<footer class="site-footer">
  <div class="wrap">
    <div class="foot-about">
      <h2>Call Us 1 – 800 – 555 – 0147</h2>
      <p>When employees feel alone during a threat-ening situation, we give them a way to let the right resources know that they need help so you can feel confident that your staff is protected</p>
      <a class="brand" href="#"><span class="brand-dot"></span><span class="brand-name">CrewBeacon</span></a>
    </div>
    <div class="foot-col">
      <h3>SHOP</h3>
      <ul><li>Add Ons</li><li>Start My Demo</li><li>Custom Quote</li><li>Start Trial</li></ul>
    </div>
    <div class="foot-col" style="width:216px">
      <h3>ABOUT</h3>
      <ul><li>Affiliates</li><li>Contact</li><li>Support</li><li>Existing Customers</li><li>Industries</li><li>Blog</li><li>FAQ</li></ul>
    </div>
    <div class="foot-col">
      <h3>LEGAL</h3>
      <ul><li>Privacy Policy</li><li>Terms of Use</li><li>End User License</li><li>Agreement</li></ul>
    </div>
  </div>
</footer>
<div class="site-bottom">2020 CrewBeacon.example, All Rights Reserved</div>

</body>
</html>
```